Redesign of key pages of website

We have a website in development: (You can see the test version here: https://staging.pawvira.ai) We want a redesign of a) the home page, b) the set up screens (all four steps), c) the account home page, and the chat page (all four linked below). It needs to look amazing in both desktop and mobile. Also, the chat page needs to have a few different versions to give people a choice between them.

Four areas:
1) Home page: https://staging.pawvira.ai/
2) Account pages: https://staging.pawvira.ai/account/chatsettings.php?step=1
3) Account home page (you'll need to set up an account which is free): https://staging.pawvira.ai/account/summary.php
4) Chat page: https://staging.pawvira.ai/chat.php?id=375

Also to clarify re: code, I don't need any of the interaction/behavior code. I just need the basic HTML and stylesheets so I can integrate that into the existing website.

Please feel free to pass by early versions to me or if you have any clarifications, let me know!

Industry/Entity Type

small businesses

Coding

Coded - Design and coding required

Number of Pages Required

5+ page

Font styles to use
Other font styles liked:
• keep the current font.

Requirements
Must have
• All the same elements/functionality on the current site. Just want a redesign. Also keep the dog visual. Also must work great in mobile and desktop and be really fun and modern and easy.
Nice to have
• Also in the setup pages, need a much better form of navigation (currently just have four circles.)

```html
<!DOCTYPE html>
<html lang="en">
<head>
<meta charset="utf-8">
<title>Pawvira – Home</title>
<link rel="stylesheet" href="https://fonts.googleapis.com/css2?family=Raleway:wght@400;500;600;700&display=swap">
<style>
:root{
  --blue:#3f87f5;
  --blue-bright:#4a8df7;
  --navy:#2b3a6b;
  --coral:#fb6b6b;
  --ink:#333b47;
  --hero-bg:#f3f6fe;
  --sky:#d6f0fb;
  --pale:#e8f1fe;
  --white:#ffffff;
  --mascot-light:#c9d6ff;
  --mascot-mid:#8fb1fb;
  --mascot-deep:#4a86f0;
}
*{box-sizing:border-box;margin:0;padding:0}
html,body{width:1200px;height:2732px;overflow:hidden}
body{position:relative;font-family:"Raleway",sans-serif;color:var(--ink);background:var(--white)}
.abs{position:absolute}
.btn{position:absolute;display:flex;align-items:center;justify-content:center;border-radius:20px;color:var(--white);font-size:14px;font-weight:500;text-decoration:none;white-space:nowrap}
.btn--blue{background:var(--blue)}
.btn--coral{background:var(--coral)}

/* hero */
.hero{position:absolute;left:0;top:0;width:1200px;height:636px;background:var(--hero-bg);border-radius:0 0 50px 50px}
.logo{position:absolute;left:60px;top:14px;font-size:44px;font-weight:700;color:var(--blue);letter-spacing:-.5px}
.nav{position:absolute;top:31px;left:600px;font-size:14px}
.nav a{position:absolute;white-space:nowrap;color:var(--ink);text-decoration:none}
.nav a.is-active{color:var(--blue)}
.hero__title{position:absolute;left:61px;top:212px;font-size:44px;font-weight:700;color:var(--ink)}
.hero__lead{position:absolute;left:61px;top:270px;width:520px;font-size:35px;line-height:40px;font-weight:700;color:var(--blue)}
.hero__photo{position:absolute;left:645px;top:210px;width:495px;height:341px;border-radius:42px;background:linear-gradient(135deg,#6b4a3a 0%,#c88a3a 45%,#e9b94a 70%,#5a4a48 100%);border:2px solid var(--navy)}
.mascot{position:absolute;border-radius:42% 42% 38% 38%;background:linear-gradient(160deg,var(--mascot-light) 0%,var(--mascot-mid) 55%,var(--mascot-deep) 100%)}

/* customize */
.section-title{position:absolute;font-size:38px;font-weight:700;color:var(--blue)}
.section-text{position:absolute;font-size:15px;line-height:23px;color:var(--ink)}
.chat-window{position:absolute;left:158px;top:878px;width:584px;height:344px;border:3px solid var(--navy);border-radius:18px;background:var(--white);overflow:hidden}
.chat-window__bar{height:36px;background:var(--navy);display:flex;align-items:center;gap:8px;padding-left:26px}
.chat-window__bar span{width:8px;height:8px;border-radius:50%;background:var(--white)}
.chat-window__bar span:nth-child(2){background:var(--blue)}
.chat-avatar{position:absolute;left:47px;top:42px;width:67px;height:69px;border-radius:50%;background:linear-gradient(160deg,#b9876a,#e7c2a6)}
.chat-name{position:absolute;left:135px;top:52px;font-size:19px;font-weight:700;color:var(--blue)}
.chat-role{position:absolute;left:135px;top:84px;font-size:13.5px}
.chat-bubble{position:absolute;left:38px;top:121px;width:473px;height:74px;border-radius:12px;background:var(--sky);padding:16px 22px;font-size:14.5px;line-height:23px;color:var(--ink)}
.chat-input{position:absolute;left:44px;top:271px;width:474px;height:46px;border-radius:24px;background:var(--blue);color:var(--white);font-size:14.5px;display:flex;align-items:center;padding-left:22px;box-shadow:0 3px 0 #a8c8fb}
.chat-send{position:absolute;right:5px;top:5px;width:36px;height:36px;border-radius:50%;background:var(--white);display:flex;align-items:center;justify-content:center}
.social{position:absolute;width:56px;height:56px;border-radius:50%;background:var(--white);border:1.5px solid;display:flex;align-items:center;justify-content:center;font-size:9.5px;font-weight:600;white-space:nowrap}

/* qualify */
.qualify{position:absolute;left:0;top:1306px;width:1200px;height:620px;background:var(--blue);border-radius:50px 50px 0 0}
.qualify__title{position:absolute;left:0;width:1200px;top:1370px;text-align:center;font-size:40px;font-weight:700;color:var(--white)}
.qualify__text{position:absolute;left:0;width:1200px;top:1423px;text-align:center;font-size:15px;line-height:23px;color:var(--white)}
.person-disc{position:absolute;left:175px;top:1620px;width:160px;height:180px;border-radius:50%;border:1.5px solid #cfe0fd;background:linear-gradient(180deg,#3f87f5 0%,#f36a6a 60%,#2b2b3a 100%)}
.scheduler{position:absolute;left:316px;top:1503px;width:583px;height:380px;border:4px solid #a8c8fb;border-bottom:none;border-radius:18px 18px 0 0;background:var(--white);overflow:hidden}
.scheduler__head{height:46px;background:var(--blue);color:var(--white);font-size:19px;font-weight:700;text-align:center;line-height:46px}
.scheduler__month{position:absolute;left:0;width:381px;top:62px;text-align:center;font-size:15px;font-weight:600}
.scheduler__month i{position:absolute;top:-2px;font-style:normal;color:var(--blue);font-size:22px}
.times{position:absolute;left:381px;top:46px;width:198px;bottom:0;background:var(--pale)}
.times__head{height:52px;background:var(--white);border-bottom:3px solid var(--blue);text-align:center;line-height:52px;font-size:16px;font-weight:600}
.times__slot{height:50px;text-align:center;line-height:50px;font-size:16px;font-weight:700;color:var(--navy)}
.times__slot--busy{background:var(--coral);color:var(--white)}
.cal{position:absolute;font-size:15px;color:var(--ink);transform:translateX(-50%)}
.cal--head{font-size:13.5px}
.cal-row{position:absolute;height:30px;border-radius:15px;background:#e8eef9}
.cal-sel{position:absolute;width:32px;height:32px;border-radius:50%;background:#1f6ae0;color:var(--white);font-size:14px;display:flex;align-items:center;justify-content:center}

/* leads */
.white-cap{position:absolute;left:0;top:1857px;width:1200px;height:200px;background:var(--white);border-radius:50px 50px 0 0}
.lead{position:absolute;border-radius:40px 40px 40px 0;color:var(--white);font-size:16px;line-height:27px}
.lead--blue{left:600px;top:1959px;width:391px;height:156px;background:var(--blue);padding:20px 0 0 49px}
.lead--coral{left:605px;top:2125px;width:391px;height:133px;background:var(--coral);padding:17px 0 0 50px;line-height:25.5px}
.lead-tail{position:absolute;width:26px;height:28px}
.email-pill{position:absolute;left:926px;width:215px;height:42px;border-radius:21px 21px 0 21px;color:var(--white);font-size:13.5px;display:flex;align-items:center;padding-left:18px;gap:10px;white-space:nowrap}
.email-pill--coral{top:1979px;background:var(--coral)}
.email-pill--blue{top:2147px;background:var(--blue)}

/* cta */
.cta{position:absolute;left:0;top:2378px;width:1200px;height:316px;background:var(--navy);border-radius:50px 50px 0 0}
.cta__title{position:absolute;left:0;width:1200px;top:2452px;text-align:center;font-size:40px;line-height:50px;font-weight:700;color:var(--white)}
.footer{position:absolute;left:0;top:2694px;width:1200px;height:38px;background:var(--blue-bright);color:var(--white);font-size:14px;display:flex;align-items:center;justify-content:space-between;padding:0 140px 0 62px}
.footer a{color:var(--navy);text-decoration:underline}
</style>
</head>
<body>

<section class="hero"></section>
<div class="logo">Pawvira</div>
<nav class="nav">
  <a class="is-active" href="https://staging.pawvira.ai/" style="left:1px">Home</a>
  <a href="https://staging.pawvira.ai/account/chatsettings.php?step=1" style="left:80px">Account</a>
  <a href="https://staging.pawvira.ai/account/summary.php" style="left:172px">Account home</a>
  <a href="https://staging.pawvira.ai/chat.php?id=375" style="left:306px">Chat</a>
</nav>
<a class="btn btn--blue" style="left:975px;top:21px;width:165px;height:38px">Login Or Register</a>

<h1 class="hero__title">Welcome!</h1>
<p class="hero__lead">Vira talks to your leads, qualifies them, and gets them on your calendar.</p>
<a class="btn btn--blue" style="left:60px;top:433px;width:165px;height:37px">See an Example!</a>
<a class="btn btn--coral" style="left:233px;top:433px;width:198px;height:37px">Create Your Vira Now</a>

<svg class="abs" style="left:590px;top:520px" width="60" height="120" viewBox="0 0 60 120"><path d="M55 0 V116 M55 40 C55 70 40 110 6 116" fill="none" stroke="var(--navy)" stroke-width="1"/></svg>
<div class="hero__photo" role="img" aria-label="Photo of a smiling woman in a yellow sweater typing on a laptop, with chat bubble graphics and a small robot icon"></div>
<div class="mascot" style="left:957px;top:145px;width:96px;height:67px" role="img" aria-label="Blue cartoon dog mascot peeking over the photo"></div>

<h2 class="section-title" style="left:61px;top:710px">Customize and share</h2>
<p class="section-text" style="left:61px;top:763px;width:480px">Customize the appearance, conversation, and much more. You can then share Vira by embedding it in your website or via a personalized link.</p>

<div class="chat-window">
  <div class="chat-window__bar"><span></span><span></span><span></span></div>
  <div class="chat-avatar" role="img" aria-label="Portrait of the salon owner"></div>
  <div class="chat-name">Mara Styles</div>
  <div class="chat-role">Hairdresser/Stylist</div>
  <div class="chat-bubble">Hello! I'm Nora's AI assistant and I'm exted to learn about your event planning needs. First, What's your name?</div>
  <div class="mascot" style="left:73px;top:203px;width:47px;height:51px" role="img" aria-label="Small blue dog mascot as chat avatar"></div>
  <div class="chat-input">Enter Your Massage...
    <span class="chat-send"><svg width="20" height="20" viewBox="0 0 24 24"><path d="M3 11 L21 3 L14 21 L11 13 Z M11 13 L21 3" fill="none" stroke="var(--coral)" stroke-width="1.6" stroke-linejoin="round"/></svg></span>
  </div>
</div>
<div class="abs" style="left:90px;top:1155px;width:96px;height:85px;border-radius:50%;background:linear-gradient(135deg,#f4f6fb,#c9d6ff)" role="img" aria-label="Line illustration of a man working at a computer"></div>
<svg class="abs" style="left:50px;top:1220px" width="60" height="60" viewBox="0 0 60 60"><path d="M2 2 C4 35 25 55 56 55" fill="none" stroke="var(--navy)" stroke-width="1"/></svg>

<svg class="abs" style="left:742px;top:930px" width="130" height="220" viewBox="0 0 130 220">
  <path d="M0 106 C30 106 25 20 80 7" fill="none" stroke="#3b7de0" stroke-width="1"/>
  <path d="M0 106 C60 106 90 80 132 69" fill="none" stroke="#2aa9e0" stroke-width="1"/>
  <path d="M0 106 C45 106 50 150 118 150" fill="none" stroke="#9b4fd0" stroke-width="1"/>
  <path d="M0 106 C30 106 40 190 88 207" fill="none" stroke="#e0306a" stroke-width="1"/>
</svg>
<div class="social" style="left:822px;top:909px;border-color:#3b7de0;color:#3b7de0">Friendly</div>
<div class="social" style="left:874px;top:971px;border-color:#2aa9e0;color:#2aa9e0">Chirp</div>
<div class="social" style="left:860px;top:1053px;border-color:#9b4fd0;color:#9b4fd0">Snapgram</div>
<div class="social" style="left:829px;top:1109px;border-color:#e0306a;color:#e0306a">Clipz</div>

<section class="qualify"></section>
<h2 class="qualify__title">Qualify and schedule</h2>
<p class="qualify__text">Get the information you need from your customers. After they meet<br>your criteria, they can book a meeting directly on your calendar.</p>
<div class="person-disc" role="img" aria-label="Illustration of a woman in a coral top holding a phone"></div>

<div class="scheduler">
  <div class="scheduler__head">Select a Date &amp; Time</div>
  <div class="scheduler__month"><i style="left:119px">&lsaquo;</i>June 2023<i style="left:250px">&rsaquo;</i></div>
  <div class="times">
    <div class="times__head">Time</div>
    <div class="times__slot">10:00am</div>
    <div class="times__slot times__slot--busy">11:00am</div>
    <div class="times__slot">11:03am</div>
    <div class="times__slot times__slot--busy">12:00am</div>
    <div class="times__slot">1:00am</div>
  </div>
  <div class="cal-row" style="left:234px;top:136px;width:106px"></div>
  <div class="cal-row" style="left:20px;top:174px;width:339px"></div>
  <div class="cal-row" style="left:59px;top:210px;width:304px"></div>
  <div class="cal-sel" style="left:154px;top:209px">11</div>

  <span class="cal cal--head" style="left:48px;top:115px">SUN</span>
  <span class="cal cal--head" style="left:104px;top:115px">MON</span>
  <span class="cal cal--head" style="left:165px;top:115px">WED</span>
  <span class="cal cal--head" style="left:223px;top:115px">TUE</span>
  <span class="cal cal--head" style="left:279px;top:115px">FRI</span>
  <span class="cal cal--head" style="left:332px;top:115px">SAT</span>

  <span class="cal" style="left:279px;top:143px">1</span><span class="cal" style="left:332px;top:143px">2</span>

  <span class="cal" style="left:45px;top:180px">3</span><span class="cal" style="left:101px;top:180px">4</span><span class="cal" style="left:169px;top:180px">5</span><span class="cal" style="left:229px;top:180px">6</span><span class="cal" style="left:281px;top:180px">7</span><span class="cal" style="left:332px;top:180px">8</span>

  <span class="cal" style="left:45px;top:216px">9</span><span class="cal" style="left:102px;top:216px">10</span><span class="cal" style="left:229px;top:216px">12</span><span class="cal" style="left:280px;top:216px">13</span><span class="cal" style="left:332px;top:216px">14</span>

  <span class="cal" style="left:48px;top:247px">15</span><span class="cal" style="left:103px;top:247px">16</span><span class="cal" style="left:170px;top:247px">17</span><span class="cal" style="left:230px;top:247px">18</span><span class="cal" style="left:282px;top:247px">19</span><span class="cal" style="left:331px;top:247px">20</span>

  <span class="cal" style="left:48px;top:283px">21</span><span class="cal" style="left:103px;top:283px">22</span><span class="cal" style="left:171px;top:283px">23</span><span class="cal" style="left:234px;top:283px">24</span><span class="cal" style="left:289px;top:283px">25</span><span class="cal" style="left:337px;top:283px">26</span>

  <span class="cal" style="left:48px;top:314px">27</span><span class="cal" style="left:103px;top:314px">28</span><span class="cal" style="left:166px;top:314px">29</span><span class="cal" style="left:234px;top:314px">30</span>
</div>

<section class="white-cap"></section>
<h2 class="section-title" style="left:61px;top:1970px">Manage your leads</h2>
<p class="section-text" style="left:61px;top:2020px;width:500px">Get notified via email or text. See a summary of each lead and manage them in one place. Search, sort, add notes, and more.</p>

<div class="lead lead--blue">Intrested in fitness Coach<br>Does not Currenly work Out<br>Specifically intrested in arms and strength<br>In the Seattle area and flexible on time.</div>
<svg class="lead-tail" style="left:600px;top:2113px" viewBox="0 0 26 28"><path d="M0 0 H26 C10 4 2 14 0 28 Z" fill="var(--blue)"/></svg>
<div class="lead lead--coral">Intrested in new fitness coach<br>Works Out 3 times a week<br>Has fitness instructor now but his<br>approach is too relaxed</div>
<svg class="lead-tail" style="left:605px;top:2256px" viewBox="0 0 26 28"><path d="M0 0 H26 C10 4 2 14 0 28 Z" fill="var(--coral)"/></svg>

<div class="email-pill email-pill--coral">
  <svg width="16" height="12" viewBox="0 0 16 12"><rect x=".75" y=".75" width="14.5" height="10.5" rx="1.5" fill="none" stroke="#fff" stroke-width="1.3"/><path d="M1 1.5 L8 7 L15 1.5" fill="none" stroke="#fff" stroke-width="1.3"/></svg>
  ben.carver@mail.test
</div>
<div class="email-pill email-pill--blue">
  <svg width="16" height="12" viewBox="0 0 16 12"><rect x=".75" y=".75" width="14.5" height="10.5" rx="1.5" fill="none" stroke="#fff" stroke-width="1.3"/><path d="M1 1.5 L8 7 L15 1.5" fill="none" stroke="#fff" stroke-width="1.3"/></svg>
  lena.morrow@mail.test
</div>

<section class="cta"></section>
<div class="mascot" style="left:544px;top:2321px;width:111px;height:110px" role="img" aria-label="Blue cartoon dog mascot sitting"></div>
<h2 class="cta__title">Let Vira handle your leads<br>today!</h2>
<a class="btn btn--coral" style="left:500px;top:2590px;width:199px;height:37px">Create Your Vira Now</a>

<footer class="footer">
  <span>© 2023 Pawvira.ai. All rights reserved. <a>Terms of Use</a></span>
  <span>Have feedback? <a>Let us know!</a></span>
</footer>

</body>
</html>
```